we do all sorts of cleaning however bookings are limited!
why not chose the right cleaners for you!
pressure cleaning, window cleaning, office, end of lease clean, accommodation, industrial and commercial cleaning and house cleaning

Logo Text

Bright Nest Cleaning Service

```html
<!DOCTYPE html>
<html lang="en">
<head>
<meta charset="utf-8">
<title>Bright Nest Cleaning Service – Business Cards</title>
<link rel="stylesheet" href="https://fonts.googleapis.com/css2?family=Lato:ital,wght@0,400;0,700;0,900;1,900&display=swap">
<style>
  :root {
    --sky: #00aeef;
    --leaf: #8dc63f;
    --ink: #1c1c1d;
    --paper: #ffffff;
    --stage: #2b2b2d;
  }
  * { box-sizing: border-box; margin: 0; padding: 0; }
  html, body { width: 1200px; height: 875px; overflow: hidden; }
  body {
    background: var(--stage);
    font-family: "Lato", sans-serif;
    position: relative;
  }
  .card {
    position: absolute;
    left: 240px;
    width: 720px;
    height: 411px;
    border-radius: 22px;
    overflow: hidden;
  }
  .card--back { top: 18px; background: var(--ink); }
  .card--front { top: 446px; background: var(--paper); }

  /* back */
  .brand { text-align: center; }
  .brand__name {
    font-weight: 900;
    color: var(--sky);
    line-height: 1;
  }
  .brand__tag {
    font-weight: 900;
    color: var(--sky);
    letter-spacing: 2px;
  }
  .card--back .brand { position: absolute; top: 78px; left: 0; right: 0; }
  .card--back .brand__name { font-size: 74px; }
  .card--back .brand__tag { font-size: 24px; margin-top: 6px; }
  .pitch {
    position: absolute;
    left: 0; right: 0; top: 262px;
    text-align: center;
  }
  .pitch__question {
    color: var(--sky);
    font-weight: 900;
    font-style: italic;
    font-size: 19px;
    text-transform: uppercase;
    margin-bottom: 10px;
  }
  .pitch__services {
    color: var(--paper);
    font-size: 17px;
    line-height: 1.55;
    padding: 0 40px;
  }
  .dot { color: var(--leaf); font-weight: 900; margin: 0 6px; }

  /* front */
  .front-bg { position: absolute; inset: 0; }
  .card--front .brand {
    position: absolute;
    top: 112px; right: 40px;
    width: 300px;
  }
  .card--front .brand__name { font-size: 50px; }
  .card--front .brand__tag { font-size: 15px; margin-top: 4px; letter-spacing: 1.5px; }
  .person { position: absolute; left: 42px; top: 40px; color: var(--paper); }
  .person__name { font-weight: 900; font-size: 34px; letter-spacing: 1px; text-transform: uppercase; }
  .person__role { font-size: 18px; margin-top: 2px; }
  .contact { position: absolute; left: 42px; top: 130px; list-style: none; color: var(--paper); font-size: 16px; }
  .contact li { display: flex; align-items: flex-start; gap: 12px; line-height: 1.35; margin-bottom: 3px; }
  .contact svg { width: 15px; height: 15px; flex: none; margin-top: 3px; fill: var(--paper); }
  .notice {
    position: absolute; left: 42px; bottom: 34px;
    color: var(--paper);
    font-weight: 900; font-style: italic;
    font-size: 19px; line-height: 1.3;
    text-transform: uppercase;
  }
</style>
</head>
<body>

<section class="card card--back" aria-label="Business card back">
  <div class="brand">
    <div class="brand__name">Bright Nest</div>
    <div class="brand__tag">CLEANING SERVICE</div>
  </div>
  <div class="pitch">
    <p class="pitch__question">Why not chose the right cleaners for you!</p>
    <p class="pitch__services">
      Pressure Cleaning<span class="dot">•</span>Window Cleaning<span class="dot">•</span>Office<span class="dot">•</span>End of Lease Clean<br>
      Accommodation<span class="dot">•</span>Industrial &amp; Commercial<span class="dot">•</span>Cleaning &amp; House Cleaning
    </p>
  </div>
</section>

<section class="card card--front" aria-label="Business card front">
  <svg class="front-bg" viewBox="0 0 720 411" preserveAspectRatio="none" aria-hidden="true">
    <path d="M0 0 H320 C330 190 470 330 720 320 V411 H0 Z" fill="var(--sky)"/>
    <path d="M338 40 C352 200 480 318 650 316" fill="none" stroke="var(--leaf)" stroke-width="6" stroke-linecap="round"/>
    <path d="M326 20 C338 190 470 326 700 322" fill="none" stroke="var(--sky)" stroke-width="3" stroke-linecap="round"/>
  </svg>

  <div class="person">
    <div class="person__name">Daniel Hart</div>
    <div class="person__role">Founder &amp; CEO</div>
  </div>

  <ul class="contact">
    <li><svg viewBox="0 0 16 16"><path d="M8 0a5.5 5.5 0 0 0-5.5 5.5C2.5 10 8 16 8 16s5.5-6 5.5-10.5A5.5 5.5 0 0 0 8 0zm0 8a2.5 2.5 0 1 1 0-5 2.5 2.5 0 0 1 0 5z"/></svg><span>423 Street Address Here, City<br>State &amp; Country, ZIP Code</span></li>
    <li><svg viewBox="0 0 16 16"><path d="M3.5 1l2.5 3-1.5 2c1 2 3 4 5 5l2-1.5 3 2.5-2 2.5C7 14 2 9 1 3.5z"/></svg><span>(123) 456-7890</span></li>
    <li><svg viewBox="0 0 16 16"><path d="M4 0h8a1 1 0 0 1 1 1v14a1 1 0 0 1-1 1H4a1 1 0 0 1-1-1V1a1 1 0 0 1 1-1zm1 2v10h6V2zm3 11a1 1 0 1 0 0 2 1 1 0 0 0 0-2z"/></svg><span>(123) 456-7890</span></li>
    <li><svg viewBox="0 0 16 16"><path d="M4 1h7v4H4zM1 6h14v7h-3v2H4v-2H1zm4 5v3h6v-3z"/></svg><span>(123) 456-7890</span></li>
    <li><svg viewBox="0 0 16 16"><path d="M0 3h16v10H0zm1.5 1.2V12h13V4.2L8 9z"/></svg><span>info@yourwebsitehere.com</span></li>
    <li><svg viewBox="0 0 16 16"><path d="M8 0a8 8 0 1 0 0 16A8 8 0 0 0 8 0zm0 1.5a6.5 6.5 0 0 1 0 13 6.5 6.5 0 0 1 0-13zM5 6h6v1.5H5zm0 2.5h6V10H5z"/></svg><span>yourwebsitehere.com</span></li>
  </ul>

  <p class="notice">We do all sorts of cleaning<br>however bookings are limited!</p>

  <div class="brand">
    <div class="brand__name">Bright Nest</div>
    <div class="brand__tag">CLEANING SERVICE</div>
  </div>
</section>

</body>
</html>
```